Course flyer - evolutive design

We want to have a nice design for our course programm.
In fact we are school language, and our course programm change approximatively each 2 weeks§.
For that we need a design that we can modify each 2 weeks (only dates change ) by ourselves.
We used to have a classical design but we want to upgrade it with a modern and attractive design.
We can have 3 versions one for each city.
We have 3 offices: Tunis, Sousse & Sfax
Attached you can find old designs

Target Market(s)

students from 16 years old till retired people 76 years old

Industry/Entity Type

Education

Font styles to use
Sans Serif

Requirements
Must have
• clear timing for courses (date, days, timing)
• prices
• Adresse (each flyer has its own adress)
• phone Number
• Cool image
Should not have
• Racism
• Violence
• Too much stuff

```html
<!DOCTYPE html>
<html lang="fr">
<head>
<meta charset="utf-8">
<title>Course d'allemand – Sousse</title>
<link href="https://fonts.googleapis.com/css2?family=Montserrat:wght@400;600;700;800&family=Open+Sans:wght@400;600;700&display=swap" rel="stylesheet">
<style>
  :root{
    --bg:#d9d9d9;
    --paper:#efefef;
    --orange:#f8a71c;
    --orange-dark:#e2631c;
    --red:#e8501d;
    --green:#7fbd2e;
    --blue:#1d5fa8;
    --ink:#2b2b2b;
    --band:#3a3a3a;
    --grey-arc:#d2d2d2;
    --photo-a:#c9d3dc;
    --photo-b:#9aa6b4;
  }
  *{margin:0;padding:0;box-sizing:border-box}
  html,body{width:1200px;height:800px;overflow:hidden}
  body{background:var(--bg);font-family:"Open Sans",Arial,sans-serif;color:var(--ink)}
  .flyer{position:absolute;left:330px;top:20px;width:540px;height:760px;background:var(--paper);overflow:hidden;box-shadow:0 6px 24px rgba(0,0,0,.18)}
  .hero{position:absolute;left:0;top:0;width:540px;height:360px}
  .title-ribbon{position:absolute;left:0;top:156px;background:var(--orange);color:#fff;font-family:"Montserrat",sans-serif;font-weight:800;font-size:19px;letter-spacing:.5px;padding:10px 26px 10px 22px;clip-path:polygon(0 0,100% 0,94% 100%,0 100%)}
  .brand{position:absolute;left:34px;top:370px;display:flex;align-items:center;gap:10px;font-family:"Montserrat",sans-serif;font-weight:700;font-size:24px;line-height:30px;color:var(--ink)}
  .brand-dot{width:22px;height:22px;border-radius:50%;background:var(--green)}
  .watermark{position:absolute;left:110px;top:420px;font-family:"Montserrat",sans-serif;font-weight:800;font-size:92px;color:rgba(0,0,0,.05);white-space:nowrap;transform:rotate(-8deg)}
  .period-tag{position:absolute;right:0;top:366px;background:var(--orange);color:#fff;font-family:"Montserrat",sans-serif;font-weight:800;font-size:17px;padding:9px 30px 9px 34px;clip-path:polygon(8% 0,100% 0,100% 100%,0 100%)}
  .schedule{position:absolute;left:34px;width:480px;display:grid;grid-template-columns:150px 1fr;gap:10px}
  .schedule.intensif{top:416px}
  .schedule.extensif{top:518px}
  .type{font-family:"Montserrat",sans-serif;font-weight:800;font-size:17px;color:var(--red);padding-left:18px;position:relative;padding-top:16px}
  .type::before{content:"";position:absolute;left:0;top:20px;width:0;height:0;border-left:12px solid var(--orange);border-top:7px solid transparent;border-bottom:7px solid transparent}
  .type small{display:block;font-size:11px;font-weight:600;color:var(--orange)}
  .sessions{font-size:11px}
  .dates{font-family:"Montserrat",sans-serif;font-weight:700;color:var(--red);font-size:12px;line-height:15px;margin-bottom:2px}
  .slots{display:flex;gap:34px}
  .time{color:var(--green);font-weight:700;font-size:11px;line-height:15px}
  .level{display:flex;gap:6px;line-height:16px}
  .level b{font-family:"Montserrat",sans-serif;font-weight:800;font-size:12px;color:var(--red);width:30px}
  .level.b b{color:var(--blue)}
  .level span{font-size:10px;font-weight:600;color:var(--ink)}
  .footer{position:absolute;left:0;bottom:0;width:540px;height:128px}
  .footer-band{position:absolute;left:0;top:0;width:540px;height:112px;background:var(--band)}
  .footer-stripe{position:absolute;left:0;bottom:0;width:540px;height:16px;background:var(--orange)}
  .notes{position:absolute;left:22px;top:16px;width:270px;color:#e6e6e6;font-size:9.5px;line-height:1.45}
  .price{margin-top:6px;color:var(--orange);font-family:"Montserrat",sans-serif;font-weight:700;font-size:13px}
  .office{position:absolute;left:310px;top:0;width:230px;height:112px;background:#2f2f2f;padding:12px 16px;color:#ddd;font-size:9px;line-height:1.4}
  .city{font-family:"Montserrat",sans-serif;font-weight:800;color:var(--orange);font-size:14px;letter-spacing:2px;margin-bottom:6px}
  .contact{display:flex;gap:8px;align-items:flex-start;margin-bottom:4px}
  .contact svg{flex:none;margin-top:1px}
</style>
</head>
<body>
<main class="flyer">
  <svg class="hero" viewBox="0 0 540 360">
    <defs>
      <linearGradient id="photoTone" x1="0" y1="0" x2="1" y2="1">
        <stop offset="0" stop-color="var(--photo-a)"/>
        <stop offset="1" stop-color="var(--photo-b)"/>
      </linearGradient>
      <clipPath id="photoClip"><circle cx="230" cy="20" r="300"/></clipPath>
    </defs>
    <circle cx="255" cy="20" r="350" fill="var(--grey-arc)"/>
    <circle cx="245" cy="20" r="335" fill="var(--orange-dark)"/>
    <circle cx="238" cy="20" r="322" fill="var(--paper)"/>
    <circle cx="234" cy="20" r="312" fill="var(--orange)"/>
    <g clip-path="url(#photoClip)">
      <rect role="img" aria-label="Photo : étudiante souriante tenant des cahiers devant une bibliothèque" x="0" y="0" width="540" height="360" fill="url(#photoTone)"/>
    </g>
  </svg>
  <div class="title-ribbon">COURSE D'ALLEMAND</div>

  <div class="watermark" aria-hidden="true">Lernhaus</div>
  <div class="brand"><span class="brand-dot"></span>Lernhaus Group</div>
  <div class="period-tag">MARS - AVRIL</div>

  <section class="schedule intensif">
    <div class="type">INTENSIF<small>(Lundi - Vendredi)</small></div>
    <div class="sessions">
      <div class="dates">07/03/2016 - 25/03/2016</div>
      <div class="slots">
        <div>
          <div class="time">09h00 - 12h00</div>
          <div class="level"><b>A1.1</b><span>DKS2090</span></div>
          <div class="level"><b>A1.2</b><span>DKS2091</span></div>
          <div class="level"><b>A2.1</b><span>DKS2092</span></div>
          <div class="level"><b>A2.2</b><span>DKS2093</span></div>
        </div>
        <div>
          <div class="time">09h00 - 12h00</div>
          <div class="level b"><b>B1.1</b><span>DKS2098</span></div>
          <div class="level b"><b>B1.2</b><span>DKS2099</span></div>
          <div class="level b"><b>B2.1</b><span>DKS2094</span></div>
        </div>
      </div>
    </div>
  </section>

  <section class="schedule extensif">
    <div class="type">EXTENSIF<small>(Lundi - Vendredi)</small></div>
    <div class="sessions">
      <div class="dates">07/03/2016 - 25/03/2016</div>
      <div class="slots">
        <div>
          <div class="time">09h00 - 12h00</div>
          <div class="level"><b>A1.1</b><span>DKS2090</span></div>
          <div class="level"><b>A1.2</b><span>DKS2091</span></div>
          <div class="level"><b>A2.1</b><span>DKS2092</span></div>
          <div class="level"><b>A2.2</b><span>DKS2093</span></div>
        </div>
        <div>
          <div class="time">09h00 - 12h00</div>
          <div class="level b"><b>B1.1</b><span>DKS2098</span></div>
          <div class="level b"><b>B1.2</b><span>DKS2099</span></div>
          <div class="level b"><b>B2.1</b><span>DKS2094</span></div>
        </div>
      </div>
    </div>
  </section>

  <footer class="footer">
    <div class="footer-band"></div>
    <div class="footer-stripe"></div>
    <div class="notes">
      Toute inscription doit impérativement se faire au plus tard une semaine avant le début de course.<br>
      Nombre minimum de 4 participants requis.<br>
      L'horaire de course est susceptible d'être modifié.
      <div class="price">Prix par Module 340 TND.</div>
    </div>
    <div class="office">
      <div class="city">SOUSSE</div>
      <div class="contact">
        <svg width="12" height="12" viewBox="0 0 12 12"><circle cx="6" cy="6" r="6" fill="var(--orange)"/><path d="M6 2.5a2 2 0 0 0-2 2c0 1.5 2 4 2 4s2-2.5 2-4a2 2 0 0 0-2-2z" fill="#2f2f2f"/></svg>
        <span>12 Rue des Oliviers, Immeuble Nour (2ème étage)</span>
      </div>
      <div class="contact">
        <svg width="12" height="12" viewBox="0 0 12 12"><circle cx="6" cy="6" r="6" fill="var(--orange)"/><path d="M4 3h1.3l.6 1.5-.8.6a4 4 0 0 0 1.8 1.8l.6-.8L9 6.7V8a1 1 0 0 1-1 1A5 5 0 0 1 3 4a1 1 0 0 1 1-1z" fill="#2f2f2f"/></svg>
        <span>+216 70 000 123</span>
      </div>
      <div class="contact">
        <svg width="12" height="12" viewBox="0 0 12 12"><circle cx="6" cy="6" r="6" fill="var(--orange)"/><rect x="3" y="4" width="6" height="4" fill="#2f2f2f"/></svg>
        <span>contact@lernhaus-group.example<br>www.lernhaus-group.example</span>
      </div>
    </div>
  </footer>
</main>
</body>
</html>
```